Hangover Drink Label Design- UK. Please read fully before submitting.

Sticky label design (55mm by 50 mm ) front and back for a small drink. Simple design which has to follow the basic layout of the pictures. PLEASE READ THE MOST HAVES AND MUST NOT HAVES CAREFULLY.

Would like to see different colour options and font- layout and words as given.

Target Market(s)

For people to drink before bed after a night out.

Colors

Designer to choose colors to be used in the design.

Requirements
Must have
• See the pictures MUST have all of these words. in " ".
• Front " Kelpmoorly" "Copper Lullaby" "Hangover Prevention"
• Back " Contains" then bullet points "Milk Thistle " Electrolytes" "Taurine" "Green Tea" "Ginseng" "Ginger" and "Kelpmoorly.com" with a barcode on the bottom.
Should not have
• Pictures/ photos of anything- animals fruit etc. No other words other than on the pictures ( see must haves)"

```html
<!DOCTYPE html>
<html lang="en">
<head>
<meta charset="UTF-8">
<title>Kelpmoorly Copper Lullaby – Label Set</title>
<link rel="stylesheet" href="https://fonts.googleapis.com/css2?family=Anton&family=Oswald:wght@600&family=Montserrat:wght@500;600;700&display=swap">
<style>
  :root {
    --red: #e8151b;
    --red-deep: #d80e14;
    --paper: #ffffff;
    --paper-shade: #f3f3f3;
    --backdrop: #b9b9b9;
    --backdrop-dark: #9a9a9a;
  }
  * { margin: 0; padding: 0; box-sizing: border-box; }
  html, body { width: 1200px; height: 962px; overflow: hidden; }
  body {
    background: radial-gradient(ellipse at center, #c6c6c6 0%, var(--backdrop) 55%, var(--backdrop-dark) 100%);
    position: relative;
    font-family: 'Montserrat', sans-serif;
  }
  .label {
    position: absolute;
    top: 220px;
    width: 460px;
    height: 522px;
    background: linear-gradient(180deg, var(--paper) 0%, var(--paper-shade) 100%);
    overflow: hidden;
    box-shadow: 0 10px 30px rgba(0,0,0,0.18);
  }
  .label--front { left: 100px; }
  .label--back { left: 640px; }

  .label__band {
    position: absolute;
    left: 0; right: 0; bottom: 0;
    height: 177px;
    background: linear-gradient(180deg, var(--red) 0%, var(--red-deep) 100%);
    color: var(--paper);
    text-align: center;
    padding-top: 44px;
  }
  .band__headline {
    font-weight: 600;
    font-size: 50px;
    letter-spacing: 2px;
    line-height: 1;
  }
  .band__subline {
    font-weight: 500;
    font-size: 30px;
    letter-spacing: 2px;
    line-height: 1;
    margin-top: 8px;
  }

  /* Front */
  .brand-name {
    position: absolute;
    top: 62px;
    left: 0; right: 0;
    text-align: center;
    font-family: 'Anton', sans-serif;
    font-size: 96px;
    line-height: 1;
    color: var(--red);
    letter-spacing: 0.5px;
  }
  .product-name {
    position: absolute;
    top: 176px;
    left: 20px; right: 20px;
    height: 80px;
    background: var(--red);
    border: 3px solid var(--red-deep);
    color: var(--paper);
    font-family: 'Oswald', sans-serif;
    font-weight: 600;
    font-size: 56px;
    line-height: 74px;
    text-align: center;
    text-transform: uppercase;
    letter-spacing: 0.5px;
  }

  /* Back */
  .contents__title {
    position: absolute;
    top: 24px;
    left: 0; right: 0;
    display: flex;
    align-items: center;
    gap: 8px;
    color: var(--red);
    font-weight: 500;
    font-size: 32px;
    letter-spacing: 1.5px;
  }
  .contents__title::before,
  .contents__title::after {
    content: "";
    flex: 1;
    border-top: 2px dotted var(--red);
  }
  .contents__list {
    position: absolute;
    top: 128px;
    left: 44px; right: 30px;
    display: flex;
  }
  .contents__column {
    list-style: none;
    padding-right: 20px;
  }
  .contents__column + .contents__column {
    border-left: 2px solid var(--red);
    padding-left: 18px;
    padding-right: 0;
  }
  .contents__item {
    color: var(--red);
    font-weight: 500;
    font-size: 19px;
    line-height: 30px;
    letter-spacing: 0.5px;
    display: flex;
    align-items: center;
    gap: 5px;
  }
  .contents__item::before {
    content: "";
    width: 9px; height: 9px;
    border-radius: 50%;
    background: var(--red);
  }
  .contents__column + .contents__column .contents__item::before { width: 12px; height: 12px; }
  .web-address {
    position: absolute;
    top: 240px;
    left: 6px; right: 6px;
    border-top: 2px solid var(--red);
    border-bottom: 2px solid var(--red);
    padding: 16px 0 14px;
    text-align: center;
    color: var(--red);
    font-weight: 500;
    font-size: 38px;
    letter-spacing: 1px;
    line-height: 1;
  }
</style>
</head>
<body>
  <section class="label label--front" aria-label="Front label">
    <h1 class="brand-name">Kelpmoorly</h1>
    <h2 class="product-name">Copper Lullaby</h2>
    <div class="label__band">
      <p class="band__headline">HANGOVER</p>
      <p class="band__subline">PREVENTION</p>
    </div>
  </section>

  <section class="label label--back" aria-label="Back label">
    <h2 class="contents__title">CONTAINS</h2>
    <div class="contents__list">
      <ul class="contents__column">
        <li class="contents__item">MILK THISTLE</li>
        <li class="contents__item">ELECTROLYTES</li>
        <li class="contents__item">TAURINE</li>
      </ul>
      <ul class="contents__column">
        <li class="contents__item">GREEN TEA</li>
        <li class="contents__item">GINSENG</li>
        <li class="contents__item">GINGER</li>
      </ul>
    </div>
    <p class="web-address">KELPMOORLY.COM</p>
    <div class="label__band">
      <p class="band__headline">HANGOVER</p>
      <p class="band__subline">PREVENTION</p>
    </div>
  </section>
</body>
</html>
```